Veltrix88 Web Site

We need a new web site for a new company, Veltrix88 Pty Ltd.
The company will provide services around the Orvane Sky and Plinth 540 products.
The company theme is "Work is what you do, not where you go." We aim to separate the concepts of data and place. Our clients can access their data anywhere, any time.
The design should look modern, international and should include the Orvane Associate logo.
Updates
My existing web site is visible at http://kelvaro.net.au. I am hoping that a good designer can provide a fresh look for the business.
Three images for "Cloud" uploaded today.
Target Market(s)
Business of all kinds
Industry/Entity Type
It Company
Requirements
Nice to have
- Colors and themes might reflect Orvane look and style.

```html
<!DOCTYPE html>
<html lang="en">
<head>
<meta charset="utf-8">
<title>Veltrix88 — Cloud Data Anywhere</title>
<link href="https://fonts.googleapis.com/css2?family=Carlito:wght@400;700&family=Arimo:wght@400;700&display=swap" rel="stylesheet">
<style>
  :root {
    --brand-blue: #1d4f7f;
    --nav-blue: #1f5b94;
    --hero-dark: #0e6f8f;
    --hero-mid: #1d9cc2;
    --hero-light: #47bfe0;
    --band-grey: #eeeeee;
    --text-grey: #7a7a7a;
    --small-grey: #8a8a8a;
    --testimonial-blue: #22507f;
    --testimonial-faint: #3b6a9a;
    --clients-band: #93a9bd;
    --client-text: #3a4f63;
    --footer-grey: #f0f0f0;
    --icon-dark: #2e2e2e;
    --white: #ffffff;
  }
  * { box-sizing: border-box; margin: 0; padding: 0; }
  html, body { width: 1200px; height: 1073px; overflow: hidden; background: var(--white); }
  body { position: relative; font-family: "Carlito", "Calibri", sans-serif; color: var(--text-grey); }

  .site-header { position: absolute; left: 0; top: 0; width: 1200px; height: 103px; border-bottom: 3px solid #e6e6e6; }
  .brand { position: absolute; left: 282px; top: 20px; display: flex; align-items: center; gap: 12px; }
  .brand-dot { width: 34px; height: 34px; border-radius: 50%; background: var(--brand-blue); }
  .brand-name { font-family: "Arimo", sans-serif; font-weight: 700; font-size: 20px; color: var(--brand-blue); letter-spacing: 0.5px; }
  .main-nav { position: absolute; left: 282px; top: 70px; display: flex; gap: 20px; font-family: "Arimo", sans-serif; font-size: 10px; }
  .main-nav a { color: var(--nav-blue); text-decoration: none; }

  .hero { position: absolute; left: 0; top: 103px; width: 1200px; height: 275px;
    background: radial-gradient(ellipse at 55% 30%, var(--hero-light) 0%, var(--hero-mid) 40%, var(--hero-dark) 100%); }
  .hero-text { position: absolute; left: 283px; top: 92px; color: var(--white); font-size: 20px; line-height: 26px; }
  .hero-art { position: absolute; left: 600px; top: 25px; width: 340px; height: 235px; border-radius: 40px;
    background: radial-gradient(ellipse at center, rgba(220,245,255,0.55) 0%, rgba(120,210,240,0.25) 55%, rgba(30,150,190,0) 80%); }

  .features { position: absolute; left: 0; top: 378px; width: 1200px; height: 149px; background: var(--band-grey); }
  .feature { position: absolute; top: 325px; width: 200px; text-align: center; }
  .feature-disc { width: 104px; height: 104px; margin: 0 auto; border-radius: 50%; background: var(--white);
    border: 5px solid #e3eef3; display: flex; align-items: center; justify-content: center; }
  .feature-label { margin-top: 14px; font-size: 13px; color: var(--text-grey); font-family: "Arimo", sans-serif; }

  .info { position: absolute; top: 527px; left: 0; width: 1200px; height: 261px; }
  .info h2 { position: absolute; top: 47px; font-weight: 400; font-size: 17px; color: var(--text-grey); font-family: "Arimo", sans-serif; }
  .secure-list { position: absolute; left: 283px; top: 98px; list-style: none; font-family: "Arimo", sans-serif; font-size: 7.5px; line-height: 16.3px; color: var(--small-grey); }
  .product-box { position: absolute; top: 85px; width: 210px; height: 108px; border: 1px solid #cfcfcf; background: var(--white);
    display: flex; align-items: center; justify-content: center; gap: 8px; }
  .product-name { font-family: "Carlito", sans-serif; font-size: 26px; color: #333; }
  .product-square { width: 22px; height: 22px; background: #e67e22; }
  .product-circle { width: 26px; height: 26px; border-radius: 50%; background: #2d8bd6; }

  .testimonial { position: absolute; left: 0; top: 788px; width: 1200px; height: 135px; background: var(--testimonial-blue); }
  .testimonial-title { position: absolute; left: 282px; top: 40px; font-family: "Arimo", sans-serif; font-weight: 700; font-size: 33px; color: var(--testimonial-faint); letter-spacing: -1px; }
  .quote-mark { position: absolute; font-family: "Arimo", sans-serif; font-weight: 700; font-size: 26px; color: var(--testimonial-faint); }
  .quote-text { position: absolute; left: 500px; top: 43px; width: 400px; font-family: "Arimo", sans-serif; font-size: 9px; line-height: 14px; color: var(--white); white-space: nowrap; }
  .quote-author { position: absolute; left: 500px; top: 90px; font-family: "Arimo", sans-serif; font-size: 9px; font-style: italic; color: var(--white); text-decoration: underline; }

  .clients { position: absolute; left: 0; top: 923px; width: 1200px; height: 66px; background: var(--clients-band); }
  .client { position: absolute; top: 24px; height: 18px; display: flex; align-items: center; justify-content: center;
    white-space: nowrap; font-family: "Carlito", sans-serif; font-weight: 700; font-size: 14px; color: var(--client-text); }

  .site-footer { position: absolute; left: 0; top: 989px; width: 1200px; height: 84px; background: var(--footer-grey); }
  .footer-nav { position: absolute; left: 282px; top: 30px; display: flex; gap: 14px; font-family: "Arimo", sans-serif; font-size: 7px; }
  .footer-nav a { color: var(--small-grey); text-decoration: none; }
  .footer-brand { position: absolute; left: 282px; top: 52px; display: flex; align-items: center; gap: 8px; }
  .footer-brand .brand-dot { width: 18px; height: 18px; }
  .footer-brand .brand-name { font-size: 11px; }
  .copyright { font-family: "Arimo", sans-serif; font-size: 7px; color: var(--small-grey); margin-left: 4px; }
  .partner-label { position: absolute; left: 810px; top: 30px; font-family: "Arimo", sans-serif; font-weight: 700; font-size: 7px; color: #333; }
  .partner-badge { position: absolute; left: 909px; top: 22px; width: 22px; height: 22px; border-radius: 50%; background: #6bbf3a; }
  .partner-name { position: absolute; left: 810px; top: 48px; font-family: "Carlito", sans-serif; font-weight: 700; font-size: 15px; color: #222; }
</style>
</head>
<body>
  <header class="site-header">
    <div class="brand"><span class="brand-dot"></span><span class="brand-name">VELTRIX88</span></div>
    <nav class="main-nav">
      <a href="#">Home</a><a href="#">Cloud Services</a><a href="#">Emergency Services</a><a href="#">Testimonials</a><a href="#">Our Clients</a><a href="#">About Us</a>
    </nav>
  </header>

  <section class="hero">
    <p class="hero-text">Cloud Data Anywhere<br>We help your business and your people<br>work anywhere, any time</p>
    <div class="hero-art" role="img" aria-label="Illustration of a cloud with gears, support headset and globe, linked by arrows to laptops, phones, servers and a padlock"></div>
  </section>

  <section class="features"></section>

  <div class="feature" style="left:297px">
    <div class="feature-disc">
      <svg width="52" height="52" viewBox="0 0 52 52" aria-hidden="true">
        <circle cx="26" cy="26" r="23" fill="none" stroke="var(--icon-dark)" stroke-width="3"/>
        <ellipse cx="26" cy="26" rx="10" ry="23" fill="none" stroke="var(--icon-dark)" stroke-width="2.5"/>
        <line x1="3" y1="26" x2="49" y2="26" stroke="var(--icon-dark)" stroke-width="2.5"/>
        <line x1="7" y1="14" x2="45" y2="14" stroke="var(--icon-dark)" stroke-width="2"/>
        <line x1="7" y1="38" x2="45" y2="38" stroke="var(--icon-dark)" stroke-width="2"/>
      </svg>
    </div>
    <div class="feature-label">Worldwide</div>
  </div>
  <div class="feature" style="left:492px">
    <div class="feature-disc">
      <svg width="48" height="52" viewBox="0 0 48 52" aria-hidden="true">
        <path d="M12 24 V16 a12 12 0 0 1 24 0 V24" fill="none" stroke="var(--icon-dark)" stroke-width="6"/>
        <rect x="4" y="22" width="40" height="28" rx="5" fill="var(--icon-dark)"/>
        <circle cx="24" cy="33" r="4" fill="var(--white)"/>
        <rect x="22" y="35" width="4" height="8" fill="var(--white)"/>
      </svg>
    </div>
    <div class="feature-label">Safe &amp; Secure</div>
  </div>
  <div class="feature" style="left:686px">
    <div class="feature-disc">
      <svg width="48" height="52" viewBox="0 0 48 52" aria-hidden="true">
        <rect x="19" y="2" width="10" height="6" fill="var(--icon-dark)"/>
        <circle cx="24" cy="29" r="19" fill="none" stroke="var(--icon-dark)" stroke-width="6"/>
        <path d="M24 29 L33 20" stroke="var(--icon-dark)" stroke-width="4"/>
        <path d="M8 44 l-4 6 l9 -1 z" fill="var(--icon-dark)"/>
      </svg>
    </div>
    <div class="feature-label">Plinth540 is anywhere</div>
  </div>

  <section class="info">
    <h2 style="left:282px">Safe &amp; Secure</h2>
    <ul class="secure-list">
      <li>Work is what you do, not where you do it</li>
      <li>Access your files, anywhere, any time</li>
      <li>Use the best skills, where ever they are</li>
      <li>Activate Orvane's Cloud services</li>
      <li>Plinth540 is anywhere you want it to be</li>
      <li>Available around the clock</li>
    </ul>
    <h2 style="left:499px">Orvane Sky</h2>
    <div class="product-box" style="left:499px"><span class="product-circle"></span><span class="product-name">Orvane Sky</span></div>
    <h2 style="left:726px">Orvane Plinth 540</h2>
    <div class="product-box" style="left:726px"><span class="product-square"></span><span class="product-name">Plinth 540</span></div>
  </section>

  <section class="testimonial">
    <div class="testimonial-title">Testimonial</div>
    <span class="quote-mark" style="left:500px;top:8px">&ldquo;</span>
    <p class="quote-text">You are a legend. We have an audit in progress today and I was able to illustrate a "Live" recovery.<br>Thank you for service above and beyond the call of duty. We really appreciate that</p>
    <span class="quote-mark" style="left:880px;top:60px">&rdquo;</span>
    <a class="quote-author">Marcus Hendley, Tallow Ridge Planning</a>
  </section>

  <section class="clients">
    <span class="client" style="left:282px;width:74px">Brightcot</span>
    <span class="client" style="left:395px;width:50px">Harbek</span>
    <span class="client" style="left:483px;width:46px">Wellnet</span>
    <span class="client" style="left:566px;width:56px">Ironcape</span>
    <span class="client" style="left:642px;width:163px">Corvell Perth</span>
    <span class="client" style="left:826px;width:46px">Quillon</span>
  </section>

  <footer class="site-footer">
    <nav class="footer-nav">
      <a href="#">Home</a><a href="#">Cloud Services</a><a href="#">Emergency Services</a><a href="#">Testimonials</a><a href="#">Our Clients</a><a href="#">About Us</a>
    </nav>
    <div class="footer-brand"><span class="brand-dot"></span><span class="brand-name">VELTRIX88</span><span class="copyright">&copy; All Right Reserved. 2013 VELTRIX88</span></div>
    <span class="partner-label">Business Partner</span>
    <span class="partner-badge"></span>
    <span class="partner-name">Orvane Associate</span>
  </footer>
</body>
</html>
```